Velmar Industrial Coatings

We are looking to improve our business cards. Our company installs industrial floor and wall coatings in industrial, chemical and food processing plants.
Our coatings which consist of epoxy, urethane, and vinyl esters provide chemical and abrasion resistant surface with non-skid properties that are easy to clean.

Target Market(s)

food manufacturing, chemical plants, breweries and wineries, warehouses, clean room floors.

Industry/Entity Type

Construction

Contact Information for Business Card

improved current logo.

Colors

Designer to choose colors to be used in the design.

Requirements
Must have
• the information from uploaded file
Nice to have
• "We'll be outstanding on your floors."

```html
<!DOCTYPE html>
<html lang="en">
<head>
<meta charset="utf-8">
<title>Velmar Industrial Coatings – Business Card</title>
<link href="https://fonts.googleapis.com/css2?family=Overpass:wght@400;600;800&display=swap" rel="stylesheet">
<style>
  :root {
    --backdrop: #b5b5b5;
    --ink: #111111;
    --card-dark: #121212;
    --card-light: #f2f2f2;
    --spray: #5a5a5a;
    --white: #ffffff;
  }
  * { margin: 0; padding: 0; box-sizing: border-box; }
  html, body { width: 1200px; height: 1010px; overflow: hidden; }
  body {
    background: var(--backdrop);
    font-family: "Overpass", sans-serif;
    color: var(--ink);
    position: relative;
  }
  .card { position: absolute; overflow: hidden; }

  /* Front */
  .card-front {
    left: 303px; top: 143px; width: 591px; height: 337px;
    background: var(--card-dark);
  }
  .spray-texture {
    position: absolute; inset: 0;
    background:
      radial-gradient(ellipse 75% 45% at 75% 52%, rgba(110,110,110,0.55), rgba(60,60,60,0.25) 60%, transparent 100%),
      linear-gradient(100deg, transparent 0%, rgba(70,70,70,0.35) 40%, rgba(80,80,80,0.45) 100%);
  }
  .front-name {
    position: absolute; left: 0; right: 0; top: 118px;
    text-align: center;
    font-weight: 800; font-size: 102px; letter-spacing: 2px;
    line-height: 1; color: #161616;
  }

  /* Back */
  .card-back {
    left: 313px; top: 571px; width: 571px; height: 326px;
    background: var(--card-light);
  }
  .brand {
    position: absolute; left: 0; right: 0; top: 18px; text-align: center;
  }
  .brand-name {
    font-weight: 800; font-size: 38px; line-height: 1; letter-spacing: 1px;
  }
  .brand-sub {
    font-weight: 800; font-size: 8.5px; letter-spacing: 0.6px; margin-top: 4px;
  }
  .person {
    position: absolute; left: 0; right: 0; top: 90px; text-align: center;
  }
  .person-name { font-size: 25px; font-weight: 400; line-height: 1; letter-spacing: 0.5px; }
  .person-phone { font-size: 14px; margin-top: 4px; }
  .contact-list {
    position: absolute; left: 0; right: 0; top: 154px;
    list-style: none; text-align: center; font-size: 14.5px;
  }
  .contact-list li { height: 27.5px; line-height: 27.5px; }
  .icon-rail {
    position: absolute; top: 140px; width: 36px; height: 186px;
    background: var(--card-dark);
    display: flex; flex-direction: column; align-items: center;
    padding-top: 14px; gap: 9.5px;
  }
  .icon-rail.left { left: 0; }
  .icon-rail.right { right: 0; }
  .icon-rail svg { width: 18px; height: 18px; fill: var(--white); }
</style>
</head>
<body>

<section class="card card-front" aria-label="Card front">
  <div class="spray-texture" role="img" aria-label="Speckled spray-coating texture fanning across the card"></div>
  <div class="front-name">VELMAR</div>
</section>

<section class="card card-back" aria-label="Card back">
  <div class="brand">
    <div class="brand-name">VELMAR</div>
    <div class="brand-sub">INDUSTRIAL COATINGS INC.</div>
  </div>

  <div class="person">
    <div class="person-name">LENA HART</div>
    <div class="person-phone">1-800-555-0142</div>
  </div>

  <ul class="contact-list">
    <li>Velmar Inc. PO Box 42 Alder, WA 98500</li>
    <li>www.velmarfloors.com</li>
    <li>Email: lena@velmarfloors.com</li>
    <li>Office: (360) 555-0131</li>
    <li>Fax: (360) 555-0133</li>
    <li>Cell: (360) 555-0177</li>
  </ul>

  <div class="icon-rail left" aria-hidden="true">
    <svg viewBox="0 0 24 24"><path d="M12 1a8 8 0 0 0-8 8c0 6 8 14 8 14s8-8 8-14a8 8 0 0 0-8-8zm0 11a3 3 0 1 1 0-6 3 3 0 0 1 0 6z"/></svg>
    <svg viewBox="0 0 24 24"><path d="M12 1a11 11 0 1 0 0 22 11 11 0 0 0 0-22zm1 2.1c1.6.5 3 2.6 3.5 5.4H13V3.1zm-2 0v5.4H7.5C8 5.7 9.4 3.6 11 3.1zM3.3 10.5h4c-.1.5-.1 1-.1 1.5s0 1 .1 1.5h-4a9 9 0 0 1 0-3zm2 5h2.3c.4 1.3.9 2.5 1.6 3.4a9 9 0 0 1-3.9-3.4zM11 20.9c-1.6-.5-3-2.6-3.5-5.4H11v5.4zm2 0v-5.4h3.5c-.5 2.8-1.9 4.9-3.5 5.4zm3.7-7.4c.1-.5.1-1 .1-1.5s0-1-.1-1.5h4a9 9 0 0 1 0 3h-4zM9.3 10.5h5.4c.1.5.1 1 .1 1.5s0 1-.1 1.5H9.3c-.1-.5-.1-1-.1-1.5s0-1 .1-1.5zm9.4-2h-2.3c-.4-1.3-.9-2.5-1.6-3.4a9 9 0 0 1 3.9 3.4zM8.8 5.1c-.7.9-1.2 2.1-1.6 3.4H5.3a9 9 0 0 1 3.5-3.4z"/></svg>
    <svg viewBox="0 0 24 24"><path d="M2 5h20v14H2V5zm2 2v.6l8 5.6 8-5.6V7H4zm0 3v7h16v-7l-8 5.6L4 10z"/></svg>
    <svg viewBox="0 0 24 24"><path d="M2 3h4v18H2V3zm5 1h3v16H7V4zm4 1h11v15H11V5zm2 2v3h7V7h-7zm0 5v2h2v-2h-2zm3 0v2h2v-2h-2zm3 0v2h1v-2h-1zm-6 3v2h2v-2h-2zm3 0v2h2v-2h-2zm3 0v2h1v-2h-1z"/></svg>
    <svg viewBox="0 0 24 24"><path d="M6 2h12v5H6V2zM2 8h20v9h-3v5H5v-5H2V8zm5 7v5h10v-5H7zm1 1h8v1H8v-1zm0 2h8v1H8v-1z"/></svg>
    <svg viewBox="0 0 24 24"><path d="M7 1h10a2 2 0 0 1 2 2v18a2 2 0 0 1-2 2H7a2 2 0 0 1-2-2V3a2 2 0 0 1 2-2zm0 3v14h10V4H7zm5 15.2a1 1 0 1 0 0 2 1 1 0 0 0 0-2z"/></svg>
  </div>

  <div class="icon-rail right" aria-hidden="true">
    <svg viewBox="0 0 24 24"><path d="M12 1a8 8 0 0 0-8 8c0 6 8 14 8 14s8-8 8-14a8 8 0 0 0-8-8zm0 11a3 3 0 1 1 0-6 3 3 0 0 1 0 6z"/></svg>
    <svg viewBox="0 0 24 24"><path d="M12 1a11 11 0 1 0 0 22 11 11 0 0 0 0-22zm1 2.1c1.6.5 3 2.6 3.5 5.4H13V3.1zm-2 0v5.4H7.5C8 5.7 9.4 3.6 11 3.1zM3.3 10.5h4c-.1.5-.1 1-.1 1.5s0 1 .1 1.5h-4a9 9 0 0 1 0-3zm2 5h2.3c.4 1.3.9 2.5 1.6 3.4a9 9 0 0 1-3.9-3.4zM11 20.9c-1.6-.5-3-2.6-3.5-5.4H11v5.4zm2 0v-5.4h3.5c-.5 2.8-1.9 4.9-3.5 5.4zm3.7-7.4c.1-.5.1-1 .1-1.5s0-1-.1-1.5h4a9 9 0 0 1 0 3h-4zM9.3 10.5h5.4c.1.5.1 1 .1 1.5s0 1-.1 1.5H9.3c-.1-.5-.1-1-.1-1.5s0-1 .1-1.5zm9.4-2h-2.3c-.4-1.3-.9-2.5-1.6-3.4a9 9 0 0 1 3.9 3.4zM8.8 5.1c-.7.9-1.2 2.1-1.6 3.4H5.3a9 9 0 0 1 3.5-3.4z"/></svg>
    <svg viewBox="0 0 24 24"><path d="M2 5h20v14H2V5zm2 2v.6l8 5.6 8-5.6V7H4zm0 3v7h16v-7l-8 5.6L4 10z"/></svg>
    <svg viewBox="0 0 24 24"><path d="M2 3h4v18H2V3zm5 1h3v16H7V4zm4 1h11v15H11V5zm2 2v3h7V7h-7zm0 5v2h2v-2h-2zm3 0v2h2v-2h-2zm3 0v2h1v-2h-1zm-6 3v2h2v-2h-2zm3 0v2h2v-2h-2zm3 0v2h1v-2h-1z"/></svg>
    <svg viewBox="0 0 24 24"><path d="M6 2h12v5H6V2zM2 8h20v9h-3v5H5v-5H2V8zm5 7v5h10v-5H7zm1 1h8v1H8v-1zm0 2h8v1H8v-1z"/></svg>
    <svg viewBox="0 0 24 24"><path d="M7 1h10a2 2 0 0 1 2 2v18a2 2 0 0 1-2 2H7a2 2 0 0 1-2-2V3a2 2 0 0 1 2-2zm0 3v14h10V4H7zm5 15.2a1 1 0 1 0 0 2 1 1 0 0 0 0-2z"/></svg>
  </div>
</section>

</body>
</html>
```